Tidewell Marketing company is looking for a web page design

Your projects should contain:

1. Header: Logo provided by us.
2. Top nav bar: offer, about us, experience, contact.
3. “Choose language” button.
4. Main section: panoramic picture (static, professional, modern).
5. Below section: 3 blocks (image+title+description), which represent our 3 main activities (titles):
• Market Research,
• Marketing Plans,
• Marketing Project.
6. ‘Contact us’ form – Message (text: “Write your message and give us details about your company and activities”), Email, SEND).
7. Page footer: (4 section: Contact, Social Media, Blog, Partners).
Updates

Hello!

I uploaded new file 'general_look', which is our idea how the page should generally look like.

BUT! it doesn't mean that your projects should look exactly like this project e.g.:
* titles Market Research, Marketing Plans, Marketing Project can be above these: Image 1,2,3.
* everything doesn't have to be in square and rectangle shape. You can try to manipulate with blocks and can add elipse elemnts or something similar.

We will appreciate your innovative ideas. Just wanted to give you general plan of the site and ilustrate all elements that we require.

Best Regards,
Benedek

IMPORTENT

Please remember that the main picture should be panoramic. Please do not close it in frame.

Target Market(s)

Small and middle sized companies, which would like to export their goods and services abroad and are interested in raising funds from Northgate Trade Council to expand their activities. These are rather industrial companies with low level of innovativeness. Our mission is to build image of the client’s company and increase awareness of their products to improve their competitiveness and innovativeness.

Industry/Entity Type

It Company

Requirements
Must have
• 1. Create designs of main page and subpage.
2. Subpage: Logo, Header, language button, place for article, navigation menu on the right side - below it “contact us” button , footer on the bottom. (In this section we are looking mainly for the design of the header and navigation menu).
3. The whole design should be a series of horizontal blocks.
4. Your projects should be associated with features such as: Reliability, Security, Professionalism, Openness, Uniqueness.
5. The design should be simple, fresh, readable, easy to use and should create a feeling of high quality services.
6. Possibility to change the panoramic picture (separate layer in a graphic file).
7. All pictures and blocks should be static, no movements.
8. Style of the page should be compliant with the logo design, font: Swiss.
9. Designs that we like: http://www.fernvale-studio.pl/, http://www.plumquarry.com/.
Should not have
• There shouldn’t be any distractions and not matching parts (whole design should be compact and easy to interpret and remember).

```html
<!DOCTYPE html>
<html lang="en">
<head>
<meta charset="utf-8">
<title>Tidewell Marketing</title>
<link rel="stylesheet" href="https://fonts.googleapis.com/css2?family=Open+Sans:wght@400;600&family=Overlock:wght@400;700&display=swap">
<style>
  :root {
    --sky: #1c8fe0;
    --page: #aecbe0;
    --panel: #dcebfa;
    --panel-edge: #c3d6e8;
    --ink: #1d2b3a;
    --navy: #0f3d5c;
    --accent: #1a7fcf;
    --title: #1b6fb5;
    --field: #93c6ee;
    --field-shadow: #4f6577;
    --rule: #1f6fae;
  }
  * { box-sizing: border-box; margin: 0; padding: 0; }
  html, body { width: 970px; height: 1200px; overflow: hidden; }
  body {
    position: relative;
    background: var(--page);
    font-family: "Open Sans", Arial, sans-serif;
    color: var(--ink);
  }
  .top-band {
    position: absolute; left: 0; top: 0; width: 970px; height: 156px;
    background: linear-gradient(180deg, #1b8de0 0%, #1f93e4 100%);
  }
  .brand {
    position: absolute; left: 83px; top: 26px;
    display: flex; align-items: center; gap: 12px;
  }
  .brand-mark {
    width: 64px; height: 64px; border-radius: 50%;
    background: var(--navy);
  }
  .brand-name {
    font-weight: 600; font-size: 40px; line-height: 1;
    color: var(--navy); letter-spacing: -1px;
  }
  .brand-tagline {
    font-size: 15px; color: var(--navy); margin-top: 4px; padding-left: 60px;
  }
  .language-button {
    position: absolute; left: 780px; top: 44px; width: 128px; height: 28px; line-height: 26px;
    font-size: 12px; color: var(--navy); text-align: center;
    background: linear-gradient(180deg, #f2f7fc 0%, #cfe0f1 100%);
    border: 1px solid #aac3da; border-radius: 4px;
    box-shadow: 0 1px 2px rgba(0,0,0,.15);
  }
  .stage {
    position: absolute; left: 79px; top: 115px; width: 829px; height: 455px;
    background: var(--panel); border-radius: 6px 6px 0 0;
  }
  .main-nav {
    display: flex; height: 42px;
    background: linear-gradient(180deg, #eef5fd 0%, #d6e6f6 100%);
    border-radius: 6px 6px 0 0;
  }
  .main-nav a {
    flex: 1; text-align: center; line-height: 42px;
    font-size: 12px; color: var(--ink); text-decoration: none;
    border-right: 1px solid #c9dbed;
  }
  .main-nav a:last-child { border-right: 0; }
  .main-nav a.is-current { color: var(--accent); }
  .hero {
    position: absolute; left: 0; top: 42px; width: 829px; height: 388px;
    background: linear-gradient(180deg, #7d86b8 0%, #c7a9c6 40%, #f0c79a 72%, #6d7f98 100%);
  }
  .hero-headline {
    position: absolute; left: 451px; top: 122px; width: 360px;
    font-family: "Overlock", "Trebuchet MS", sans-serif;
    font-size: 38px; line-height: 42px; color: #0e3e63;
  }
  .btn {
    display: inline-block; font-size: 11px; color: var(--accent);
    background: linear-gradient(180deg, #f2f7fc 0%, #cfe0f1 100%);
    border: 1px solid #aac3da; border-radius: 4px;
    text-align: center; box-shadow: 0 1px 2px rgba(0,0,0,.15);
  }
  .hero .btn {
    position: absolute; left: 672px; top: 351px; width: 124px; height: 33px; line-height: 31px;
  }
  .service {
    position: absolute; top: 559px; width: 262px; height: 282px;
    background: var(--panel); border: 1px solid var(--panel-edge);
  }
  .service-photo {
    position: absolute; left: 4px; top: 0; width: 254px; height: 142px; border-radius: 4px;
  }
  .service h2 {
    position: absolute; left: 19px; top: 160px;
    font-family: "Overlock", "Trebuchet MS", sans-serif;
    font-weight: 400; font-size: 19px; color: var(--title);
  }
  .service p {
    position: absolute; left: 19px; top: 194px; width: 210px;
    font-size: 12px; line-height: 16px; color: var(--ink);
  }
  .service .btn {
    position: absolute; right: 18px; top: 248px; width: 88px; height: 26px; line-height: 24px;
  }
  .photo-ruins { background: linear-gradient(180deg, #a9b6c0 0%, #5c7a4e 55%, #7b6a4f 100%); }
  .photo-bridge { background: linear-gradient(180deg, #3f7fd0 0%, #6fb1d8 45%, #2f8a9e 70%, #8c7a46 100%); }
  .photo-city { background: linear-gradient(180deg, #1d2436 0%, #3a3f50 50%, #8a6a3e 100%); }
  .field {
    position: absolute; background: var(--field);
    box-shadow: 6px 6px 0 var(--field-shadow);
    font-size: 12px; color: var(--ink); text-align: center;
  }
  .field-message { left: 253px; top: 893px; width: 366px; height: 69px; line-height: 69px; }
  .field-email { left: 651px; top: 893px; width: 234px; height: 28px; line-height: 28px; }
  .field-send { left: 808px; top: 930px; width: 77px; height: 26px; line-height: 26px; }
  .site-footer {
    position: absolute; left: 0; top: 998px; width: 970px; height: 163px;
    background: var(--panel); border-top: 4px solid var(--rule);
    border-bottom: 1px solid var(--rule);
  }
  .footer-col { position: absolute; top: 30px; }
  .footer-col h3 {
    font-family: "Overlock", "Trebuchet MS", sans-serif;
    font-weight: 400; font-size: 19px; color: var(--title); margin-bottom: 6px;
  }
  .footer-col li { list-style: none; font-size: 11px; line-height: 13px; color: var(--navy); padding-left: 4px; }
  .footer-col.blog li { font-size: 15px; line-height: 22px; font-weight: 600; }
  .social { position: absolute; left: 734px; top: 84px; display: flex; gap: 6px; }
  .social span { width: 30px; height: 30px; border-radius: 5px; display: block; }
  .social .s1 { background: #3b5a97; }
  .social .s2 { background: #3a3a3a; }
  .social .s3 { background: #4fb3ea; }
  .copyright { position: absolute; left: 95px; top: 137px; font-size: 9px; color: var(--ink); }
  .webmaster { position: absolute; left: 759px; top: 135px; font-size: 10px; color: var(--accent); }
</style>
</head>
<body>
  <header class="top-band">
    <div class="brand">
      <span class="brand-mark"></span>
      <div class="brand-text">
        <div class="brand-name">Tidewell Marketing</div>
        <div class="brand-tagline">your passport to foreign markets</div>
      </div>
    </div>
    <span class="language-button">Choose language</span>
  </header>

  <section class="stage">
    <nav class="main-nav">
      <a class="is-current">Home</a>
      <a>Offer</a>
      <a>About us</a>
      <a>Experience</a>
      <a>Contact</a>
    </nav>
    <div class="hero" role="img" aria-label="Panoramic photo of a sail-shaped tower hotel on the sea at sunset with a person watching">
      <p class="hero-headline">You are in the right place to expand your export</p>
      <span class="btn">Read More</span>
    </div>
  </section>

  <article class="service" style="left:79px;">
    <div class="service-photo photo-ruins" role="img" aria-label="Photo of mountain ruins among green peaks"></div>
    <h2>Market Research</h2>
    <p>Place to write something about market research</p>
    <span class="btn">Read More</span>
  </article>
  <article class="service" style="left:365px;">
    <div class="service-photo photo-bridge" role="img" aria-label="Wide-angle photo of a red suspension bridge over a bay"></div>
    <h2>Marketing Plans</h2>
    <p>Place to write something about your marketing plans</p>
    <span class="btn">Read More</span>
  </article>
  <article class="service" style="left:647px;">
    <div class="service-photo photo-city" role="img" aria-label="Night photo of city towers with light trails"></div>
    <h2>Marketing Projects</h2>
    <p>Place to write something about your marketing projects</p>
    <span class="btn">Read More</span>
  </article>

  <form class="contact-form">
    <div class="field field-message">Write your message</div>
    <div class="field field-email">Email</div>
    <div class="field field-send">SEND</div>
  </form>

  <footer class="site-footer">
    <div class="footer-col" style="left:137px;">
      <h3>Partners</h3>
      <ul><li>partner 1</li><li>partner 2</li><li>...</li></ul>
    </div>
    <div class="footer-col" style="left:315px;">
      <h3>Contact</h3>
      <ul><li>address</li><li>phone</li><li>fax</li><li>email</li></ul>
    </div>
    <div class="footer-col blog" style="left:498px;">
      <h3>Blog</h3>
      <ul><li>...</li><li>...</li></ul>
    </div>
    <div class="social" aria-label="Social media links">
      <span class="s1"></span><span class="s2"></span><span class="s3"></span>
    </div>
    <p class="copyright">Copyright 2012 Tidewell Marketing Company.</p>
    <p class="webmaster">Webmaster Login</p>
  </footer>
</body>
</html>
```